Report presentation for measurement or inline reports

First page of report. Our inline reporting will come in a maintenance map. We want a modern first page and a real eye-catcher for a new company based in the Netherlands called: PRN Luchtcomfort B.V. We are a service company witch measures, balances and give advices at indoor climate HVAC installations. We would like to see designs that use the color blue. We deliver our services to different buildings: Hospitals, atractions, officebuildings, government buildings, swimming pools and schools. Our website: www.prnlc.nl
Updates

Can you all add the new logo please. The companyname is PRN Luchtcomfort B.V.. In witch format can i retrieve the design?

Industry/Entity Type

It Company

Colors
0255a3
3176b5
85abd2
cedeed
eaf1f7
ffffff

Requirements
Must have
• Projectname; projectplace; Inline or measure report; date; logo; companyname. it must be easy printable so not to much colours.
• The companyname is: PRN Luchtcomfort B.V.. Please add the name. A new logo is updated.
Nice to have
• Maybe some pictures from hvac installations, buildings or measure

```html
<!DOCTYPE html>
<html lang="en">
<head>
<meta charset="UTF-8">
<title>Inline Report – Cover</title>
<link rel="stylesheet" href="https://fonts.googleapis.com/css2?family=Playfair+Display:wght@900&family=Montserrat:wght@400;600;700;800&display=swap">
<style>
  :root {
    --blue-deep: #1d3c8c;
    --blue-main: #0255a3;
    --blue-mid: #3176b5;
    --blue-light: #85abd2;
    --blue-pale: #cedeed;
    --blue-mist: #eaf1f7;
    --white: #ffffff;
    --ink: #111111;
    --backdrop: #ececec;
  }
  * { box-sizing: border-box; margin: 0; padding: 0; }
  html, body {
    width: 1200px; height: 767px; overflow: hidden;
    background: var(--backdrop);
  }
  .canvas {
    position: relative; width: 1200px; height: 767px;
  }
  .cover {
    position: absolute; left: 343px; top: 20px;
    width: 514px; height: 727px;
    background: var(--white);
    box-shadow: 0 6px 24px rgba(0,0,0,0.18);
    overflow: hidden;
  }
  .brand {
    position: absolute; top: 34px; left: 0; width: 100%;
    display: flex; flex-direction: column; align-items: center; gap: 6px;
    font-family: "Montserrat", sans-serif;
  }
  .brand-square {
    width: 26px; height: 26px; background: var(--blue-main);
  }
  .brand-name {
    font-size: 12px; font-weight: 700; color: var(--blue-main); letter-spacing: 0.3px;
  }
  .report-title {
    position: absolute; top: 92px; left: 0; width: 100%;
    text-align: center;
    font-family: "Playfair Display", serif; font-weight: 900;
    font-size: 56px; line-height: 0.92; color: var(--ink);
    letter-spacing: -0.5px;
  }
  .rule-thick, .rule-thin {
    position: absolute; left: 0; width: 100%;
  }
  .rule-thin { top: 219px; height: 2px; background: var(--blue-light); }
  .rule-thick { top: 224px; height: 5px; background: var(--blue-mid); }
  .panel {
    position: absolute; top: 232px; left: 0; width: 100%; bottom: 0;
    background: var(--blue-deep);
    font-family: "Montserrat", sans-serif; color: var(--white);
  }
  .project-name {
    position: absolute; top: 32px; left: 34px;
    font-size: 19px; font-weight: 800; line-height: 1.2;
    text-transform: uppercase;
  }
  .details {
    position: absolute; top: 96px; left: 34px;
    display: flex; flex-direction: column; gap: 14px;
  }
  .detail-label { font-size: 11px; font-weight: 700; }
  .detail-value { font-size: 11px; font-weight: 400; margin-top: 3px; color: var(--blue-mist); }
  .meta {
    position: absolute; top: 118px; right: 34px; text-align: right;
  }
  .meta-date { font-size: 21px; font-weight: 600; letter-spacing: 0.5px; }
  .meta-project-label { font-size: 11px; font-weight: 600; margin-top: 8px; color: var(--blue-pale); }
  .meta-project-number { font-size: 14px; font-weight: 700; }
  .skyline {
    position: absolute; left: 0; right: 0; bottom: 0; height: 262px;
    background: linear-gradient(180deg, var(--blue-deep) 0%, #3a5fa8 30%, #7f9cc4 62%, #4a5f80 82%, #2a3f63 100%);
  }
</style>
</head>
<body>
<div class="canvas">
  <article class="cover">
    <header class="brand">
      <span class="brand-square"></span>
      <span class="brand-name">PRN Solutions</span>
    </header>

    <h1 class="report-title">INLINE<br>REPORT</h1>

    <div class="rule-thin"></div>
    <div class="rule-thick"></div>

    <section class="panel">
      <h2 class="project-name">NVB Renovative<br>Fase 2 ET Utrecht</h2>

      <dl class="details">
        <div>
          <dt class="detail-label">Client :</dt>
          <dd class="detail-value">Hofstede Installatieprojecten</dd>
        </div>
        <div>
          <dt class="detail-label">Project Place :</dt>
          <dd class="detail-value">Utrecht, Netherlands</dd>
        </div>
        <div>
          <dt class="detail-label">Measured by:</dt>
          <dd class="detail-value">PRN Luchtcomfort B.V.</dd>
        </div>
      </dl>

      <div class="meta">
        <div class="meta-date">MAY 2017</div>
        <div class="meta-project-label">PROJECT:</div>
        <div class="meta-project-number">140639</div>
      </div>

      <div class="skyline" role="img" aria-label="Photograph of a city skyline with office towers along the waterfront under a blue sky"></div>
    </section>
  </article>
</div>
</body>
</html>
```